The Wisdom of Lanterns New Book Cover Design Project

Book cover design . Paperback, ebook, and Talvora (derived from book cover) files/images required.
Book Title: The Wisdom of Lanterns
Subtitle: Under Copper Bridges
Author: Daniel Forsythe
Files: Ebook, Paperback (Brindlewick & Halvern Quill), Talvora sized image
File size & information to be provided once design is ready. Brindlewick paperback will be 5.25 x 8.
Completion date is flexible. Planning to publish in November.
Updates

Target Market(s)

Motorcycle owners

Font styles to use
Sans Serif

Requirements
Must have
• A generic looking motorcycle (samples attached). Thumbnail easily recognized as a motorcycle book.
Nice to have
• Open to all ideas but am favoring my idea: to emphasize the title lettering similar to (but not a copy of) other Wisdom books (examples attached), on a plain background. All books in the category have a motorcycle on the cover. Author name and subtitle do not have to be prominent. Rider optional..
Should not have
• Should not look like a biker romance or fantasy cover or look cartoonish. Motorcycle pic should be fairly generic (brand, style,).

```html
<!DOCTYPE html>
<html lang="en">
<head>
<meta charset="utf-8">
<title>The Wisdom of Lanterns — Daniel Forsythe</title>
<link rel="stylesheet" href="https://fonts.googleapis.com/css2?family=Antonio:wght@700&family=Aleo:wght@400&display=swap">
<style>
  :root {
    --backdrop: #1b1b1b;
    --paper: #ffffff;
    --title-red: #c0272f;
    --ink: #1a1a1a;
    --bike-dark: #1e1e20;
    --bike-mid: #4a4a4e;
  }
  html, body {
    margin: 0;
    padding: 0;
    width: 1200px;
    height: 1200px;
    overflow: hidden;
    background: var(--backdrop);
  }
  .canvas {
    position: relative;
    width: 1200px;
    height: 1200px;
    background: var(--backdrop);
  }
  .book-cover {
    position: absolute;
    left: 285px;
    top: 120px;
    width: 630px;
    height: 960px;
    background: var(--paper);
  }
  .book-cover svg {
    display: block;
    width: 630px;
    height: 960px;
  }
  .title-small {
    font-family: "Antonio", "Arial Narrow", sans-serif;
    font-weight: 700;
    fill: var(--ink);
  }
  .title-large {
    font-family: "Antonio", "Arial Narrow", sans-serif;
    font-weight: 700;
    fill: var(--title-red);
  }
  .subtitle {
    font-family: "Aleo", Georgia, serif;
    font-size: 23px;
    fill: var(--ink);
  }
  .author {
    font-family: "Aleo", Georgia, serif;
    font-size: 30px;
    fill: var(--ink);
  }
</style>
</head>
<body>
<main class="canvas">
  <section class="book-cover" aria-label="Book cover: The Wisdom of Lanterns by Daniel Forsythe">
    <svg viewBox="0 0 630 960" xmlns="http://www.w3.org/2000/svg">
      <defs>
        <radialGradient id="bike-tone" cx="50%" cy="55%" r="60%">
          <stop offset="0%" stop-color="var(--bike-mid)"/>
          <stop offset="100%" stop-color="var(--bike-dark)"/>
        </radialGradient>
      </defs>

      <text class="title-small" x="112" y="133" font-size="70" textLength="57" lengthAdjust="spacingAndGlyphs">The</text>

      <text class="title-large" x="176" y="470" font-size="461" textLength="337" lengthAdjust="spacingAndGlyphs">Wisdom</text>

      <rect class="motorcycle-photo" x="109" y="476" width="289" height="194" rx="36"
            fill="url(#bike-tone)" role="img"
            aria-label="Photograph of a black classic café-racer motorcycle, seen from the rear three-quarter view"/>

      <text class="title-small" x="419" y="651" font-size="70" textLength="32" lengthAdjust="spacingAndGlyphs">of</text>

      <text class="title-large" x="114" y="790" font-size="131" textLength="400" lengthAdjust="spacingAndGlyphs">Lanterns</text>

      <text class="subtitle" x="114" y="821">Under Copper Bridges</text>

      <text class="author" x="161" y="930" textLength="309" lengthAdjust="spacing">Daniel Forsythe</text>
    </svg>
  </section>
</main>
</body>
</html>
```